Gleamstone Works website

Epoxy Resin Flooring for home renovations and commercial property.
3 page website homepage, contact us and gallery with a link to Snapvelle.
Looking for someone to create a visually pleasing website for home transformation and design. I have attached some designs of completed work however I can send you many more. Use colour and don’t inspiration from the logo. If happy with stage one we will add a commercial page as a new project.

Target Market(s)

Homeowners that want to improve their home or rental property

Industry/Entity Type

Home improvements

Coding

Coded - Design and coding required

Number of Pages Required

3 page

Requirements
Must have
• Home Page, Contact Us page and showcase / gallery page
Nice to have
• I would like the colour theme to be taken from the logo, a clean finish with artistic usuals to get homeowners excited about their project

```html
<!DOCTYPE html>
<html lang="en">
<head>
<meta charset="utf-8">
<title>Gleamstone Works – Epoxy Resin Flooring</title>
<link rel="stylesheet" href="https://fonts.googleapis.com/css2?family=Montserrat:wght@400;500;600;700;800&display=swap">
<style>
:root{
  --red:#e50f13;
  --ink:#141414;
  --text:#2b2b2b;
  --grey-bg:#efefef;
  --grey-mid:#d9d9d9;
  --dark:#1d1d1d;
  --white:#ffffff;
}
*{box-sizing:border-box;margin:0;padding:0}
html,body{width:1200px;height:3117px;overflow:hidden}
body{position:relative;font-family:'Montserrat',sans-serif;color:var(--text);background:var(--white)}
.abs{position:absolute}
.red{color:var(--red)}

/* header */
.site-header{position:absolute;left:0;top:0;width:1200px;height:80px;z-index:5}
.brand{position:absolute;left:111px;top:10px;display:flex;align-items:center;gap:12px}
.brand-mark{width:62px;height:62px;background:var(--red)}
.brand-name{font-weight:800;font-size:22px;color:var(--ink);line-height:1.1}
.brand-phone{font-size:14px;letter-spacing:1px;color:var(--ink)}
.main-nav a{position:absolute;top:33px;font-size:15px;font-weight:600;color:var(--ink);text-decoration:none}
.main-nav .active{color:var(--red);border-bottom:2px solid var(--red);padding-bottom:4px}
.nav-sep{position:absolute;top:34px;width:1px;height:14px;background:#999}
.social-icon{position:absolute;left:908px;top:30px}
.call-box{position:absolute;left:975px;top:0;width:225px;height:79px;background:var(--red);color:var(--white);display:flex;align-items:center;gap:12px;padding-left:26px}
.call-box .icon{width:32px;height:32px;border-radius:50%;background:var(--white);display:flex;align-items:center;justify-content:center}
.call-box small{display:block;font-size:13px}
.call-box strong{font-size:17px;font-weight:700}

/* hero */
.hero-bg{position:absolute;left:0;top:0;width:1200px;height:700px;background:linear-gradient(120deg,#f4f4f4 0%,#e4e4e4 55%,#d6d6d6 100%)}
.hero-photo{position:absolute;left:653px;top:97px;width:436px;height:538px;border-radius:48% 52% 45% 55%/38% 40% 60% 62%;background:linear-gradient(160deg,#eef0f3 0%,#b8bcc2 45%,#3f434a 80%,#5a6a3a 100%)}
.eyebrow{font-size:18px;letter-spacing:2px;color:var(--ink);display:flex;align-items:center;gap:12px}
.eyebrow::after{content:"";width:48px;height:2px;background:var(--red)}
.eyebrow.both::before{content:"";width:48px;height:2px;background:var(--red)}
.hero-title{font-weight:800;font-size:34px;line-height:44px;color:var(--ink);text-transform:uppercase}
.btn{position:absolute;display:flex;align-items:center;justify-content:center;border-radius:26px;font-size:15px;font-weight:700;color:var(--white);text-transform:uppercase;letter-spacing:.5px}
.btn-red{background:var(--red)}
.btn-dark{background:var(--ink)}

/* about */
.about-ring{position:absolute;left:90px;top:790px;width:424px;height:424px;border-radius:50%;border:5px solid var(--red);padding:8px}
.about-photo{width:100%;height:100%;border-radius:50%;background:linear-gradient(150deg,#c6ccd4 0%,#8e9aaa 30%,#3d4c62 60%,#2f3c50 100%)}
.about-small{position:absolute;left:349px;top:1071px;width:174px;height:174px;border-radius:50%;border:5px solid var(--white);background:linear-gradient(170deg,#8a6d55 0%,#c8bfb2 45%,#b6ab9c 100%)}
.about-dot{position:absolute;left:333px;top:1219px;width:36px;height:36px;border-radius:50%;background:var(--red)}
.section-title{font-weight:800;font-size:34px;color:var(--ink);text-transform:uppercase}
.about-sub{font-weight:700;font-size:21px;line-height:29px;color:var(--ink)}
.body-copy{font-size:18.5px;line-height:27px;color:#333}

/* gallery */
.gallery-bg{position:absolute;left:0;top:1355px;width:1200px;height:780px;background:linear-gradient(180deg,#ececec,#f3f3f3 50%,#e9e9e9)}
.tile{position:absolute;width:315px;height:235px}
.tile-active{background:var(--red);display:flex;align-items:center;justify-content:center}
.tile-active .frame{position:absolute;inset:10px;border:2px solid rgba(255,255,255,.8)}

/* contact */
.contact-bg{position:absolute;left:0;top:2132px;width:1200px;height:665px;background:radial-gradient(ellipse at 30% 40%,#2b2b2b 0%,#1a1a1a 60%,#121212 100%)}
.contact-item{position:absolute;left:127px;display:flex;align-items:center;gap:20px;color:var(--white)}
.contact-item .icon{width:46px;height:46px;border-radius:50%;background:var(--white);display:flex;align-items:center;justify-content:center}
.contact-item small{display:block;color:var(--red);font-size:15px}
.contact-item strong{font-weight:600;font-size:19px}
.form-card{position:absolute;left:607px;top:2275px;width:497px;height:387px;border-radius:16px;background:#ececec}
.field{position:absolute;background:var(--white);font-size:12.5px;color:#444;padding:13px 17px}

/* footer */
.foot-line{position:absolute;height:1px;background:#bbb}
.foot-nav{position:absolute;top:2856px;font-size:16px;font-weight:700;color:var(--ink)}
.foot-dot{position:absolute;top:2863px;width:6px;height:6px;border-radius:50%;background:var(--red)}
.foot-item{position:absolute;top:2946px;display:flex;align-items:center;gap:10px}
.foot-item .icon{width:34px;height:34px;border-radius:50%;background:var(--red);display:flex;align-items:center;justify-content:center}
.foot-item small{display:block;font-size:11px;font-weight:700;color:var(--ink)}
.foot-item span{font-size:15px;color:var(--ink)}
</style>
</head>
<body>

<!-- hero background -->
<div class="hero-bg" role="img" aria-label="Soft faded photo of a finished epoxy patio floor"></div>
<div class="hero-photo" role="img" aria-label="Photo of a dark speckled epoxy porch floor in a flowing organic frame"></div>
<svg class="abs" style="left:0;top:640px" width="1200" height="120" viewBox="0 0 1200 120">
  <path d="M0 26 C200 26 360 -4 540 40 C700 78 880 10 1050 18 C1130 22 1170 26 1200 26 L1200 120 L0 120Z" fill="#fff"/>
</svg>

<header class="site-header">
  <div class="brand">
    <div class="brand-mark"></div>
    <div>
      <div class="brand-name">Gleamstone Works</div>
      <div class="brand-phone">0412 386 905</div>
    </div>
  </div>
  <nav class="main-nav">
    <a class="active" style="left:478px" href="#">HOME</a>
    <span class="nav-sep" style="left:560px"></span>
    <a style="left:598px" href="#">GALLERY</a>
    <span class="nav-sep" style="left:700px"></span>
    <a style="left:739px" href="#">CONTACT US</a>
    <span class="nav-sep" style="left:862px"></span>
  </nav>
  <svg class="social-icon" width="24" height="24" viewBox="0 0 24 24" aria-label="Snapvelle"><rect x="2" y="2" width="20" height="20" rx="5" fill="none" stroke="#141414" stroke-width="2"/></svg>
  <div class="call-box">
    <div class="icon"><svg width="18" height="18" viewBox="0 0 24 24"><path d="M6.6 10.8a15 15 0 006.6 6.6l2.2-2.2c.3-.3.7-.4 1-.2 1.1.4 2.3.6 3.6.6.6 0 1 .4 1 1V20c0 .6-.4 1-1 1A17 17 0 013 4c0-.6.4-1 1-1h3.5c.6 0 1 .4 1 1 0 1.3.2 2.5.6 3.6.1.3 0 .7-.2 1z" fill="#e50f13"/></svg></div>
    <div><small>CALL US NOW</small><strong>0412 386 905</strong></div>
  </div>
</header>

<section class="hero">
  <div class="abs eyebrow" style="left:103px;top:244px">WELCOME TO GLEAMSTONE WORKS</div>
  <h1 class="abs hero-title" style="left:102px;top:278px"><span class="red">Epoxy resin flooring for</span><br>home renovations and<br>commercial property</h1>
  <a class="btn btn-red" style="left:105px;top:439px;width:185px;height:51px">Contact us</a>
  <a class="btn btn-dark" style="left:313px;top:437px;width:189px;height:51px">View gallery</a>
</section>

<div class="abs" style="left:600px;top:686px;width:3px;height:68px;background:var(--red)"></div>

<!-- about -->
<section class="about">
  <div class="about-ring"><div class="about-photo" role="img" aria-label="Photo of a tiled-look blue grey epoxy patio beside a house"></div></div>
  <div class="about-small" role="img" aria-label="Photo of a smooth beige epoxy floor in a bar area"></div>
  <div class="about-dot"></div>
  <div class="abs eyebrow" style="left:594px;top:850px">WHO WE ARE</div>
  <h2 class="abs section-title" style="left:594px;top:876px"><span class="red">About</span> Gleamstone Works</h2>
  <p class="abs about-sub" style="left:598px;top:940px;width:520px">Epoxy Resin Flooring for home renovations and commercial property</p>
  <p class="abs body-copy" style="left:598px;top:1009px;width:530px">Lorem ipsum dolor sit amet, consectetur adipiscing elit, sed do eiusmod tempor incididunt ut labore et dolore magna aliqua. Quis ipsum suspendisse ultrices</p>
  <p class="abs body-copy" style="left:598px;top:1120px;width:530px">Lorem ipsum dolor sit amet, consectetur adipiscing elit, sed do eiusmod tempor incididunt ut labore et dolore magna aliqua. Quis ipsum suspendisse ultrices gravida.</p>
</section>

<!-- gallery -->
<section class="gallery">
  <div class="gallery-bg"></div>
  <svg class="abs" style="left:0;top:1305px" width="1200" height="52" viewBox="0 0 1200 52">
    <path d="M0 52 L0 40 C180 40 380 52 520 30 C600 14 660 6 740 26 C860 54 1040 38 1200 40 L1200 52Z" fill="#ececec"/>
  </svg>
  <div class="abs eyebrow both" style="left:492px;top:1391px">OUR WORK</div>
  <h2 class="abs section-title" style="left:0;width:1206px;text-align:center;top:1418px"><span class="red">Project</span> Gallery</h2>

  <div class="tile" style="left:131px;top:1503px;background:linear-gradient(140deg,#d7d9dc,#7f8a6a 40%,#3b3f46 75%)" role="img" aria-label="Photo of a dark epoxy porch floor with potted plant"></div>
  <div class="tile tile-active" style="left:456px;top:1503px"><div class="frame"></div>
    <svg width="30" height="30" viewBox="0 0 30 30"><circle cx="15" cy="15" r="12" fill="none" stroke="#fff" stroke-width="3"/></svg></div>
  <div class="tile" style="left:781px;top:1503px;background:linear-gradient(170deg,#c9d4c8,#7c5a4c 35%,#4c5058 70%,#35383d)" role="img" aria-label="Photo of a large covered epoxy patio"></div>
  <div class="tile" style="left:131px;top:1747px;background:linear-gradient(150deg,#5a4a40,#8a8c90 40%,#5d6168 80%,#6f9a4a)" role="img" aria-label="Photo of a grey tiled epoxy floor by timber stairs"></div>
  <div class="tile" style="left:456px;top:1747px;background:linear-gradient(175deg,#7a6a5e,#c8c1b6 40%,#bcb3a6)" role="img" aria-label="Photo of a smooth beige epoxy floor"></div>
  <div class="tile" style="left:781px;top:1747px;background:linear-gradient(150deg,#aeb8c6,#4a5a72 45%,#2f3b4e 85%,#6f8a4a)" role="img" aria-label="Photo of a blue grey tiled epoxy patio"></div>

  <svg class="abs" style="left:46px;top:1708px" width="30" height="58" viewBox="0 0 30 58"><path d="M27 2 L3 29 L27 56" fill="none" stroke="#333" stroke-width="2"/></svg>
  <svg class="abs" style="left:1124px;top:1708px" width="30" height="58" viewBox="0 0 30 58"><path d="M3 2 L27 29 L3 56" fill="none" stroke="#333" stroke-width="2"/></svg>

  <a class="btn btn-red" style="left:523px;top:2021px;width:188px;height:51px">View more</a>
</section>

<!-- contact -->
<section class="contact">
  <div class="contact-bg" role="img" aria-label="Dark faded photo of an epoxy floor interior"></div>
  <svg class="abs" style="left:0;top:2740px" width="1200" height="60" viewBox="0 0 1200 60">
    <path d="M0 60 L0 56 C160 56 330 40 480 20 C560 8 640 6 720 24 C860 54 1040 56 1200 56 L1200 60Z" fill="#fff"/>
  </svg>
  <div class="abs eyebrow" style="left:127px;top:2264px;color:#fff">GET IN TOUCH</div>
  <h2 class="abs section-title" style="left:127px;top:2290px;color:#fff"><span class="red">Contact</span> Epoxy</h2>
  <p class="abs" style="left:127px;top:2348px;width:440px;font-size:18.5px;line-height:27px;color:#fff">Lorem ipsum dolor sit amet, consectetur adipiscing elit sed do eiusmod temp</p>

  <div class="contact-item" style="top:2441px">
    <div class="icon"><svg width="24" height="24" viewBox="0 0 24 24"><path d="M6.6 10.8a15 15 0 006.6 6.6l2.2-2.2c.3-.3.7-.4 1-.2 1.1.4 2.3.6 3.6.6.6 0 1 .4 1 1V20c0 .6-.4 1-1 1A17 17 0 013 4c0-.6.4-1 1-1h3.5c.6 0 1 .4 1 1 0 1.3.2 2.5.6 3.6.1.3 0 .7-.2 1z" fill="#141414"/></svg></div>
    <div><small>Phone Number</small><strong style="font-weight:700;font-size:21px">0412 386 905</strong></div>
  </div>
  <div class="contact-item" style="top:2513px">
    <div class="icon"><svg width="24" height="18" viewBox="0 0 24 18"><rect x="1" y="1" width="22" height="16" rx="2" fill="none" stroke="#141414" stroke-width="2"/><path d="M1 2 L12 10 L23 2" fill="none" stroke="#141414" stroke-width="2"/></svg></div>
    <div><small>Email address</small><strong>info@gleamstoneworks.com</strong></div>
  </div>
  <div class="contact-item" style="top:2585px">
    <div class="icon"><svg width="20" height="26" viewBox="0 0 20 26"><path d="M10 1a9 9 0 00-9 9c0 7 9 15 9 15s9-8 9-15a9 9 0 00-9-9z" fill="#141414"/><circle cx="10" cy="10" r="3.5" fill="#fff"/></svg></div>
    <div><small>Location</small><strong>123 Street Avenue address line</strong></div>
  </div>

  <form class="form-card">
    <h3 class="abs" style="left:49px;top:38px;font-size:20px;font-weight:700;color:#222">LEAVE US A MESSAGE</h3>
    <div class="field" style="left:48px;top:88px;width:198px;height:40px">First Name</div>
    <div class="field" style="left:255px;top:88px;width:199px;height:40px">Last Name</div>
    <div class="field" style="left:48px;top:139px;width:198px;height:41px">Email address</div>
    <div class="field" style="left:255px;top:139px;width:199px;height:41px">Phone</div>
    <div class="field" style="left:48px;top:188px;width:406px;height:86px">Message</div>
    <div class="btn btn-red" style="left:48px;top:294px;width:187px;height:45px;font-size:14px">Send message</div>
  </form>
</section>

<!-- footer -->
<footer>
  <div class="foot-line" style="left:109px;top:2834px;width:369px"></div>
  <div class="foot-line" style="left:109px;top:2894px;width:369px"></div>
  <div class="foot-line" style="left:718px;top:2834px;width:369px"></div>
  <div class="foot-line" style="left:718px;top:2894px;width:369px"></div>
  <a class="foot-nav" style="left:172px">HOME</a>
  <span class="foot-dot" style="left:264px"></span>
  <a class="foot-nav" style="left:301px">ABOUT US</a>
  <a class="foot-nav" style="left:769px">GALLERY</a>
  <span class="foot-dot" style="left:880px"></span>
  <a class="foot-nav" style="left:918px">CONTACT US</a>

  <div class="brand" style="left:505px;top:2832px;gap:10px">
    <div class="brand-mark" style="width:60px;height:62px"></div>
    <div>
      <div class="brand-name" style="font-size:18px">Gleamstone Works</div>
      <div class="brand-phone" style="font-size:13px">0412 386 905</div>
    </div>
  </div>

  <div class="foot-item" style="left:143px">
    <div class="icon"><svg width="16" height="16" viewBox="0 0 24 24"><path d="M6.6 10.8a15 15 0 006.6 6.6l2.2-2.2c.3-.3.7-.4 1-.2 1.1.4 2.3.6 3.6.6.6 0 1 .4 1 1V20c0 .6-.4 1-1 1A17 17 0 013 4c0-.6.4-1 1-1h3.5c.6 0 1 .4 1 1 0 1.3.2 2.5.6 3.6.1.3 0 .7-.2 1z" fill="#fff"/></svg></div>
    <div><small>PHONE</small><span>0412 386 905</span></div>
  </div>
  <div class="foot-item" style="left:351px">
    <div class="icon"><svg width="16" height="12" viewBox="0 0 24 18"><rect x="1" y="1" width="22" height="16" rx="2" fill="none" stroke="#fff" stroke-width="2"/><path d="M1 2 L12 10 L23 2" fill="none" stroke="#fff" stroke-width="2"/></svg></div>
    <div><small>EMAIL ADDRESS</small><span>info@gleamstoneworks.com</span></div>
  </div>
  <div class="foot-item" style="left:623px">
    <div class="icon"><svg width="14" height="18" viewBox="0 0 20 26"><path d="M10 1a9 9 0 00-9 9c0 7 9 15 9 15s9-8 9-15a9 9 0 00-9-9z" fill="#fff"/><circle cx="10" cy="10" r="3.5" fill="#e50f13"/></svg></div>
    <div><small>LOCATION</small><span>123 Street Avenue address</span></div>
  </div>
  <div class="foot-item" style="left:910px">
    <div class="icon"><svg width="16" height="16" viewBox="0 0 24 24"><rect x="3" y="3" width="18" height="18" rx="5" fill="none" stroke="#fff" stroke-width="2.4"/></svg></div>
    <div><small>SNAPVELLE</small><span>@gleamstoneworks</span></div>
  </div>

  <div class="foot-line" style="left:126px;top:3019px;width:959px"></div>
  <p class="abs" style="left:0;width:1200px;text-align:center;top:3042px;font-size:12.5px;color:#222">Copyright © 2024 <u>Gleamstone Works</u>. All Right Reserved</p>
  <div class="abs" style="left:1019px;top:3037px;width:36px;height:36px;border-radius:50%;background:#e6e6e6;display:flex;align-items:center;justify-content:center">
    <svg width="12" height="8" viewBox="0 0 12 8"><path d="M1 7 L6 2 L11 7" fill="none" stroke="#555" stroke-width="1.6"/></svg>
  </div>
</footer>

</body>
</html>
```